Email signature and business card

Australian company called Tarrowin. We provide construction and maintenance services to the mining industry. I would like the design to be similar to our website theme(www.tarrowin.com.au) whilst staying compact. RGB colours to include: 42,96,140 and 232,163,0 and I have attached 2 logos.

The following fields will need to be included:

Full Name
Title
Location/Project
Phone
Mobile
Fax
Email
Web site

Target Market(s)

Mining Industry

Industry/Entity Type

Construction

Requirements
Must have
• Full Name, Title, Office Address, Phone, Mobile, Fax, Email, Web address
• Back of card must include: Boilermaking, Carpentry, Concrete, Construction, Cranes, Data and Comms, Electrical, Fabrication, Fitting, Labour Hire, Plumbing, Rigging, Shutdowns

```html
<!DOCTYPE html>
<html lang="en">
<head>
<meta charset="utf-8">
<title>Tarrowin – Email Signature Business Card</title>
<link href="https://fonts.googleapis.com/css2?family=Roboto+Condensed:wght@400;700&family=Raleway:wght@500;600&display=swap" rel="stylesheet">
<style>
  :root {
    --brand-blue: #1a5f8b;
    --name-blue: #0e4d75;
    --brand-gold: #e8a300;
    --card-light: #7ccbdc;
    --card-mid: #2f8fae;
    --card-dark: #0d5879;
    --panel-pale: #f1f5f8;
    --panel-white: #ffffff;
    --panel-sky: #c6dcf2;
    --stage-grey: #dadada;
    --note-teal: #1f5a76;
    --arrow-red: #c8262c;
    --button-dark: #3a3a3a;
    --white: #ffffff;
  }
  * { box-sizing: border-box; margin: 0; padding: 0; }
  html, body { width: 1200px; height: 979px; overflow: hidden; }
  body { position: relative; font-family: "Roboto Condensed", Arial, sans-serif; background: var(--stage-grey); }

  .stage { position: absolute; inset: 0; background: radial-gradient(ellipse at 85% 20%, #f2f2f2 0%, var(--stage-grey) 65%); }

  .variant { position: absolute; left: 0; width: 599px; }
  .variant--one { top: 0; height: 326px; background: var(--panel-pale); }
  .variant--two { top: 326px; height: 327px; background: var(--panel-white); }
  .variant--three { top: 653px; height: 326px; background: var(--panel-sky); }
  .variant-label {
    position: absolute; right: 27px; bottom: 12px;
    font-family: "Raleway", Arial, sans-serif; font-weight: 600; font-size: 13px;
    letter-spacing: 2px; color: var(--note-teal);
  }

  .card {
    position: absolute; left: 117px; top: 45px; width: 368px; height: 232px;
    border-radius: 8px; overflow: hidden; color: var(--white);
    background: linear-gradient(168deg, var(--card-light) 0%, var(--card-mid) 42%, var(--card-dark) 100%);
    box-shadow: 0 6px 8px -3px rgba(0,0,0,0.35), inset 0 1px 0 rgba(255,255,255,0.7);
    border: 1px solid #0b4c6a;
  }
  .card::before {
    content: ""; position: absolute; left: -40px; top: 62px; width: 460px; height: 70px;
    background: linear-gradient(180deg, rgba(255,255,255,0.18), rgba(255,255,255,0));
    transform: rotate(-6deg);
  }
  .card-brand {
    position: absolute; left: 33px; top: 18px;
    font-weight: 700; font-size: 27px; letter-spacing: 0.5px; color: var(--brand-blue);
  }
  .card-photo {
    position: absolute; left: 258px; top: 12px; width: 80px; height: 77px;
    border: 4px solid var(--white); box-shadow: 0 2px 4px rgba(0,0,0,0.3);
    background: linear-gradient(180deg, #d7e9fa 0%, #8fbbe6 100%);
  }
  .card-emblem {
    position: absolute; left: 294px; top: 12px; width: 56px; height: 60px;
    border-radius: 50%; background: #124f72;
  }
  .card-name { position: absolute; left: 30px; top: 70px; font-weight: 700; font-size: 23px; color: var(--name-blue); }
  .card-title { position: absolute; left: 30px; top: 94px; font-weight: 700; font-size: 15.5px; }
  .card-rule { position: absolute; left: 0; right: 0; top: 123px; height: 1px; background: rgba(255,255,255,0.45); }
  .card-details { position: absolute; left: 30px; top: 131px; font-size: 13px; line-height: 16.5px; }
  .card-details strong { font-weight: 700; font-size: 13.5px; }
  .card-details .field { font-weight: 400; }
  .card--labels-gold .field { color: #f3c231; }
  .card-web { position: absolute; left: 30px; top: 197px; font-weight: 700; font-size: 16px; }
  .card-download {
    position: absolute; left: 239px; top: 188px; width: 92px; height: 34px;
    display: flex; border-radius: 3px; overflow: hidden;
    background: var(--button-dark); border: 1px solid #1d1d1d;
    box-shadow: 0 1px 0 rgba(255,255,255,0.3);
  }
  .card-download .icon { width: 30px; border-right: 1px solid #222; display: flex; align-items: center; justify-content: center; background: #444; }
  .card-download .text { flex: 1; font-size: 11.5px; line-height: 13px; padding: 3px 0 0 4px; }
  .card-screw {
    position: absolute; width: 10px; height: 10px; border-radius: 50%;
    background: radial-gradient(circle at 35% 35%, #f4f4f4, #8a8a8a);
    border: 1px solid #555;
  }

  .notice, .notes, .file-count, .file-list {
    position: absolute; font-family: "Raleway", Arial, sans-serif; font-weight: 500;
    color: var(--note-teal); letter-spacing: 1.6px; text-transform: uppercase;
  }
  .notice { left: 638px; top: 13px; font-size: 12.5px; }
  .notes { left: 638px; top: 793px; font-size: 12.5px; line-height: 15.5px; }
  .file-count { left: 638px; top: 922px; font-size: 12.5px; font-weight: 600; }
  .file-divider { position: absolute; left: 760px; top: 906px; width: 2px; height: 46px; background: var(--note-teal); }
  .file-list { left: 793px; top: 912px; font-size: 12.5px; font-weight: 600; line-height: 18.5px; }
  .file-tick { position: absolute; left: 773px; top: 914px; }
  .pointer { position: absolute; left: 550px; top: 800px; }
</style>
</head>
<body>
<main class="stage">

  <section class="variant variant--one">
    <article class="card">
      <div class="card-brand">TARROWIN</div>
      <div class="card-photo" role="img" aria-label="Employee portrait photo"></div>
      <div class="card-name">Callum J. HARTLEY</div>
      <div class="card-title">General Manager Safety &amp; Environment</div>
      <div class="card-rule"></div>
      <div class="card-details">
        <strong>Level 3, 14 Harbour Road, Palm Ridge QLD 4580</strong><br>
        <span class="field">Phone:</span> <strong>(07) 5550 1200</strong> &nbsp;|&nbsp; <span class="field">Fax:</span> <strong>(07) 5550 1299</strong><br>
        <span class="field">Mobile:</span> <strong>(04) 5550 3141</strong><br>
        <span class="field">E-mail:</span> <strong>callum@tarrowin.com.au</strong>
      </div>
      <div class="card-web">www.tarrowin.com.au</div>
      <div class="card-download">
        <span class="icon"><svg width="10" height="10" viewBox="0 0 10 10"><path d="M1 2h8L5 7z" fill="#e8a300"/><rect x="1" y="8" width="8" height="1.5" fill="#ddd"/></svg></span>
        <span class="text">Download<br>VCard (.vcf)</span>
      </div>
    </article>
    <span class="variant-label">VAR. 1</span>
  </section>

  <section class="variant variant--two">
    <article class="card">
      <div class="card-brand">TARROWIN</div>
      <div class="card-emblem" role="img" aria-label="Company bird emblem"></div>
      <div class="card-name">Callum J. HARTLEY</div>
      <div class="card-title">General Manager Safety &amp; Environment</div>
      <div class="card-rule"></div>
      <div class="card-details">
        <strong>Level 3, 14 Harbour Road, Palm Ridge QLD 4580</strong><br>
        <span class="field">Phone:</span> <strong>(07) 5550 1200</strong> &nbsp;|&nbsp; <span class="field">Fax:</span> <strong>(07) 5550 1299</strong><br>
        <span class="field">Mobile:</span> <strong>(04) 5550 3141</strong><br>
        <span class="field">E-mail:</span> <strong>callum@tarrowin.com.au</strong>
      </div>
      <div class="card-web">www.tarrowin.com.au</div>
      <div class="card-download">
        <span class="icon"><svg width="10" height="10" viewBox="0 0 10 10"><path d="M1 2h8L5 7z" fill="#e8a300"/><rect x="1" y="8" width="8" height="1.5" fill="#ddd"/></svg></span>
        <span class="text">Download<br>VCard (.vcf)</span>
      </div>
    </article>
    <span class="variant-label">VAR. 2</span>
  </section>

  <section class="variant variant--three">
    <article class="card card--labels-gold">
      <span class="card-screw" style="left:6px;top:6px"></span>
      <span class="card-screw" style="right:6px;top:6px"></span>
      <span class="card-screw" style="left:6px;bottom:6px"></span>
      <span class="card-screw" style="right:6px;bottom:6px"></span>
      <div class="card-brand">TARROWIN</div>
      <div class="card-photo" role="img" aria-label="Employee portrait photo"></div>
      <div class="card-name">Callum J. HARTLEY</div>
      <div class="card-title">General Manager Safety &amp; Environment</div>
      <div class="card-rule"></div>
      <div class="card-details">
        <strong>Level 3, 14 Harbour Road, Palm Ridge QLD 4580</strong><br>
        <span class="field">Phone:</span> <strong>(07) 5550 1200</strong> &nbsp;|&nbsp; <span class="field">Fax:</span> <strong>(07) 5550 1299</strong><br>
        <span class="field">Mobile:</span> <strong>(04) 5550 3141</strong><br>
        <span class="field">E-mail:</span> <strong>callum@tarrowin.com.au</strong>
      </div>
      <div class="card-web">www.tarrowin.com.au</div>
      <div class="card-download">
        <span class="icon"><svg width="10" height="10" viewBox="0 0 10 10"><path d="M1 2h8L5 7z" fill="#e8a300"/><rect x="1" y="8" width="8" height="1.5" fill="#ddd"/></svg></span>
        <span class="text">Download<br>VCard (.vcf)</span>
      </div>
    </article>
    <span class="variant-label">VAR. 3</span>
  </section>

  <p class="notice">Please view this image at 100% zoom</p>

  <svg class="pointer" width="90" height="60" viewBox="0 0 90 60" aria-hidden="true">
    <path d="M84 4 C60 8 30 24 8 50" fill="none" stroke="var(--arrow-red)" stroke-width="2"/>
    <path d="M3 55 L8 40 L16 52 Z" fill="var(--arrow-red)"/>
  </svg>

  <p class="notes">
    Transparent PNG, works with any background color.<br>
    PSD source well organized, easy to replace text.<br>
    Free fonts used (Roboto Condensed).<br>
    Possibility to use or not employee photos.<br>
    Possibility to link to a *.vcf business card.
  </p>

  <p class="file-count">File #1 of 2</p>
  <span class="file-divider"></span>
  <svg class="file-tick" width="13" height="11" viewBox="0 0 13 11" aria-hidden="true">
    <path d="M1 6 L5 10 L12 1" fill="none" stroke="var(--arrow-red)" stroke-width="2.4"/>
  </svg>
  <p class="file-list">Email signature<br>Business card</p>

</main>
</body>
</html>
```